Torvane Travel Business Card Design

We need a new business card design for our travel agency business - Torvane Travel. We design packages to some of the most popular travel destinations in the world for groups, individuals and also tailor-make personalised packages. Our logo attached must be used. On the back of the card we would like a list of all websites under our Torvane brand to be posted. We would like clean, modern, simple design.

Industry/Entity Type

Travel Agent

Contact Information for Business Card

Owen Pridmore
National Sales Manager
Reservations: 1300 742 689
Tel: 61 28473 5096
Fax: 61 2847 3971
Email: owen@torvanetravel.com.au
Web: www.torvanetravel.com.au

Address: Level 1, 417 Harwick Street
Sydney NSW 2000 Australia

Requirements
Must have
• On the back of the card we want all websites listed under our Torvane brand.
• Torvane Travel Group - Wholesale Specialists
• www.qpjourneys.com.au - New Caledonia
• www.bravelmijourneys.com.au - Tahiti
• www.sorvenbreakhub.com.au - China
Nice to have
• Modern, clean lined, simple and fresh
Should not have
• Look dull

```html
<!DOCTYPE html>
<html lang="en">
<head>
<meta charset="utf-8">
<title>Torvane Travel Business Card</title>
<link rel="stylesheet" href="https://fonts.googleapis.com/css2?family=Source+Sans+3:wght@400;600&display=swap">
<style>
  :root {
    --navy: #2b2a7e;
    --red: #e5171f;
    --ink: #4a4a4a;
    --card: #f7f7f7;
    --bg: #e6e6e6;
    --rule: #5a59a0;
  }
  * { margin: 0; padding: 0; box-sizing: border-box; }
  html, body { width: 1200px; height: 750px; overflow: hidden; }
  body {
    background: var(--bg);
    font-family: "Source Sans 3", sans-serif;
    position: relative;
  }
  .card {
    position: absolute;
    top: 228px;
    width: 461px;
    height: 263px;
    background: var(--card);
  }
  .card--front { left: 124px; }
  .card--back { left: 618px; }

  .holder { position: absolute; left: 30px; top: 40px; }
  .holder__name {
    color: var(--navy);
    font-size: 17px;
    font-weight: 600;
    letter-spacing: 0.2px;
    line-height: 20px;
  }
  .holder__role {
    color: var(--red);
    font-size: 13px;
    line-height: 18px;
  }
  .rule {
    position: absolute;
    top: 87px;
    height: 1px;
    background: var(--rule);
  }
  .rule--left { left: 0; width: 221px; }
  .rule--right { left: 356px; right: 0; }

  .hero-plane {
    position: absolute;
    left: 210px;
    top: 36px;
    width: 231px;
    height: 102px;
    background: linear-gradient(120deg, #e5171f, #ef3a40);
    border-radius: 40px 8px 50px 8px;
  }

  .address {
    position: absolute;
    left: 31px;
    top: 104px;
    color: var(--ink);
    font-size: 11.5px;
    line-height: 15px;
  }
  .contacts {
    position: absolute;
    left: 30px;
    top: 139px;
    list-style: none;
  }
  .contacts li {
    display: flex;
    align-items: center;
    height: 17.6px;
    color: var(--ink);
    font-size: 11.5px;
  }
  .contacts svg { width: 12px; height: 12px; margin-right: 9px; flex: none; }
  .contacts small { font-size: 10px; margin-left: 3px; }

  .group {
    position: absolute;
    right: 29px;
    top: 170px;
    text-align: right;
  }
  .group__title {
    color: var(--navy);
    font-size: 12px;
    font-weight: 600;
    line-height: 15px;
  }
  .group__sites {
    list-style: none;
    color: var(--ink);
    font-size: 10px;
    line-height: 13.2px;
  }

  .brand {
    position: absolute;
    left: 0;
    right: 0;
    top: 108px;
    text-align: center;
    color: var(--navy);
    font-size: 44px;
    font-weight: 600;
    letter-spacing: -0.5px;
    line-height: 50px;
  }
</style>
</head>
<body>
  <section class="card card--front">
    <div class="holder">
      <p class="holder__name">OWEN PRIDMORE</p>
      <p class="holder__role">NATIONAL SALES MANAGER</p>
    </div>
    <div class="rule rule--left"></div>
    <div class="rule rule--right"></div>
    <div class="hero-plane" role="img" aria-label="Large red silhouette of a passenger jet climbing to the right"></div>

    <p class="address">Level 1, 417 Harwick Street<br>Sydney NSW 2000 Australia</p>

    <ul class="contacts">
      <li>
        <svg viewBox="0 0 12 12"><path fill="#2b2a7e" d="M2.5 0.8l2 2.2-1 1.4c.6 1.4 1.6 2.4 3 3l1.4-1 2.2 2-1.3 1.8C5 10 1.8 6.8 0.6 2.2z"/></svg>
        1300 742 689 <small>(Reservations)</small>
      </li>
      <li>
        <svg viewBox="0 0 12 12"><path fill="#2b2a7e" d="M2.5 0.8l2 2.2-1 1.4c.6 1.4 1.6 2.4 3 3l1.4-1 2.2 2-1.3 1.8C5 10 1.8 6.8 0.6 2.2z"/></svg>
        61 28473 5096
      </li>
      <li>
        <svg viewBox="0 0 12 12"><rect x="3" y="0.5" width="6" height="3.5" fill="none" stroke="#2b2a7e"/><rect x="0.5" y="4" width="11" height="5" fill="#2b2a7e"/><rect x="2.5" y="9" width="7" height="2.5" fill="#2b2a7e"/></svg>
        61 28473 5096
      </li>
      <li>
        <svg viewBox="0 0 12 12"><rect x="0.5" y="2.5" width="11" height="7" fill="#2b2a7e"/><path d="M1 3l5 3.5L11 3" fill="none" stroke="#f7f7f7" stroke-width="1"/></svg>
        owen@torvanetravel.com.au
      </li>
      <li>
        <svg viewBox="0 0 12 12"><circle cx="6" cy="6" r="5.5" fill="#2b2a7e"/><path d="M3 3.5c1.5 0 2 1 1.5 2S5 7.5 6 8M8 2.5c-.5 1.2.5 2 1.5 2.3" fill="none" stroke="#f7f7f7" stroke-width="1"/></svg>
        www.torvanetravel.com.au
      </li>
    </ul>

    <div class="group">
      <p class="group__title">Torvane Travel Group - Wholesale Specialists</p>
      <ul class="group__sites">
        <li>www.qpjourneys.com.au - New Caledonia</li>
        <li>www.bravelmijourneys.com.au - Tahiti</li>
        <li>www.sorvenbreakhub.com.au - China</li>
      </ul>
    </div>
  </section>

  <section class="card card--back">
    <p class="brand">Torvane Travel</p>
  </section>
</body>
</html>
```